Broschüre in Querformat für Immobilienmakler
Zielgruppe
Immobilienmakler - Überregional tätig - zielgerichtete Vermarktung - Zielgruppe sind Verkäufer oft ältere Menschen
Ich möchte eine Broschüre mit 12 Seiten im Querformat - Die Broschüre sollte der Website harvrenk-immobilien.example ein wenig ähneln.
Aufgabenstellung
klare Linie - schnell erklärbar und übersichtlich - logischer Aufbau - Aufmerksamkeit erwecken durch Bilder - schnelle Info für Querleser - VERTRAUEN - ehrlich und authentisch - nicht Eitel - schnelle Zurechtfindung - Serviceorientiert - Rundumsorglos Paket

```html
<!DOCTYPE html>
<html lang="de">
<head>
<meta charset="utf-8">
<title>Unsere Leistungen als Immobilienmakler für Sie</title>
<link rel="stylesheet" href="https://fonts.googleapis.com/css2?family=Montserrat:wght@600;700;800;900&display=swap">
<style>
  :root {
    --navy: #0f2340;
    --navy-deep: #0a1a31;
    --orange: #f5a800;
    --icon: #f4c982;
    --white: #ffffff;
    --ink: #0f2340;
    --sky-top: #6b7f9c;
    --sky-mid: #41587a;
    --sky-bottom: #26395a;
  }
  html, body {
    margin: 0;
    padding: 0;
    width: 1200px;
    height: 856px;
    overflow: hidden;
    background: var(--navy-deep);
    font-family: "Montserrat", Arial, sans-serif;
  }
  .spread {
    position: relative;
    width: 1200px;
    height: 856px;
    background: var(--navy);
    overflow: hidden;
  }
  .page-text {
    position: absolute;
    left: 23px;
    top: 0;
    width: 573px;
    height: 835px;
    background: var(--white);
  }
  .headline {
    position: absolute;
    left: 26px;
    top: 40px;
    margin: 0;
    font-size: 38px;
    line-height: 42px;
    font-weight: 800;
    letter-spacing: -0.2px;
  }
  .headline .accent { color: var(--orange); display: block; }
  .headline .main { color: var(--ink); display: block; }
  .intro, .costs-text {
    position: absolute;
    left: 191px;
    width: 360px;
    margin: 0;
    font-size: 16.5px;
    line-height: 25px;
    font-weight: 700;
    color: var(--ink);
  }
  .intro { top: 163px; }
  .costs-label {
    position: absolute;
    left: 191px;
    top: 408px;
    margin: 0;
    font-size: 16.5px;
    font-weight: 800;
    color: var(--orange);
  }
  .costs-text { top: 458px; }
  .icon {
    position: absolute;
    left: 66px;
    width: 70px;
    height: 70px;
  }
  .icon-check { top: 228px; }
  .icon-price { top: 524px; }

  .page-photo {
    position: absolute;
    left: 596px;
    top: 0;
    width: 592px;
    height: 835px;
    overflow: hidden;
  }
  .city-photo {
    position: absolute;
    inset: 0;
    background: linear-gradient(180deg, var(--sky-top) 0%, var(--sky-mid) 45%, var(--sky-bottom) 60%, #35496a 80%, #2a3d5d 100%);
  }
  .halo {
    position: absolute;
    inset: 0;
  }
  .services {
    position: absolute;
    left: 38px;
    top: 116px;
    width: 521px;
    border-collapse: collapse;
    color: var(--white);
    font-size: 15.5px;
    font-weight: 800;
  }
  .services th {
    color: var(--orange);
    font-size: 18px;
    font-weight: 800;
    text-align: left;
    padding: 0 0 28px 0;
  }
  .services th.when, .services td.when { text-align: right; }
  .services td {
    height: 48.2px;
    padding: 0;
    vertical-align: middle;
    white-space: nowrap;
  }
</style>
</head>
<body>
<main class="spread">
  <section class="page-text">
    <h1 class="headline">
      <span class="accent">Unsere Leistungen als</span>
      <span class="main">Immobilienmakler für Sie</span>
    </h1>

    <svg class="icon icon-check" viewBox="0 0 70 70" aria-hidden="true">
      <circle cx="35" cy="35" r="32" fill="none" stroke="var(--icon)" stroke-width="3"/>
      <circle cx="35" cy="35" r="22" fill="none" stroke="var(--icon)" stroke-width="2.5"/>
      <path d="M24 35 L32 43 L47 27" fill="none" stroke="var(--icon)" stroke-width="4" stroke-linecap="round" stroke-linejoin="round"/>
    </svg>

    <p class="intro">Mit der Aufstellung soll gezeigt werden, was wir „Team Harvrenk-Immobilien“ als qualifizierte Immobilienmakler für Sie erbringen. Wir gehen mit sämtlichen Leistungen in Vorleistung und werden nur bei einem erfolgreichen Kaufvertragsabschluss mit einer Provision honoriert.</p>

    <p class="costs-label">Kosten:</p>

    <svg class="icon icon-price" viewBox="0 0 70 70" aria-hidden="true">
      <circle cx="35" cy="35" r="32" fill="none" stroke="var(--icon)" stroke-width="3"/>
      <circle cx="38" cy="26" r="7" fill="none" stroke="var(--icon)" stroke-width="2.5"/>
      <path d="M17 42 L24 42 Q30 40 34 43 L42 43 Q45 44 42 47 L33 47 M24 50 L38 52 L52 42 Q55 40 53 38 L44 43" fill="none" stroke="var(--icon)" stroke-width="2.5" stroke-linecap="round" stroke-linejoin="round"/>
    </svg>

    <p class="costs-text">Unser Service in sämtlichen Phasen ist bei einem Vermarktungsauftrag mit der vereinbarten Provision abgegolten. Es entstehen Ihnen keine Mehrkosten. Wir verlangen keine Vorauszahlungen und es ist für uns eine Selbstverständlichkeit, dass wir erst nach erfolgreicher Vermittlung Ihrer Immobilie unserer Leistung in Rechnung stellen.</p>
  </section>

  <section class="page-photo">
    <div class="city-photo" role="img" aria-label="Foto einer Großstadt-Skyline am Wasser in der Dämmerung, blau getönt"></div>
    <svg class="halo" viewBox="0 0 592 835" aria-hidden="true">
      <circle cx="592" cy="455" r="375" fill="#ffffff" fill-opacity="0.12"/>
    </svg>

    <table class="services">
      <thead>
        <tr><th>Leistung:</th><th class="when">Zeitplan der Ausführung:</th></tr>
      </thead>
      <tbody>
        <tr><td>Wertermittlung</td><td class="when">maximal 3 Werktage</td></tr>
        <tr><td>Marktanalyse</td><td class="when">maximal 3 Werktage</td></tr>
        <tr><td>Erstellung des professionellen Expose</td><td class="when">4 Werktage</td></tr>
        <tr><td>Nachbearbeitung Fotos</td><td class="when">3 Werktage</td></tr>
        <tr><td>360° VR erstellen</td><td class="when">3 Werktage</td></tr>
        <tr><td>Vermarktungsbeginn</td><td class="when">maximal 4 Werktage</td></tr>
        <tr><td>Info an vorgemerkte Interessenten</td><td class="when">maximal 3 Werktage</td></tr>
        <tr><td>Erreichbarkeit</td><td class="when">täglich</td></tr>
        <tr><td>Finanzierungsangebote</td><td class="when">4 Werktage</td></tr>
        <tr><td>Veröffentlichung Homepage</td><td class="when">5 Werktage</td></tr>
        <tr><td>Erstellung Energieausweis</td><td class="when">2 Werktage</td></tr>
      </tbody>
    </table>
  </section>
</main>
</body>
</html>
```